Bref créative
Business Cards, Letterhead, and Envelope
Cordova Peak Realty Group Inc.
Simple
4236 Fernway Crest Blvd.
Marlow Springs, CA 90417
Morvani@cordovapeak.com
DRE#07246318
Pls feel Free to be creative
Bullet points or any creative design but needs following pointers
- First time buyer Programs
- Multi-Unit property Programs
- Low down payment Programs
- $ 0 Closing costs available

```html
<!DOCTYPE html>
<html lang="en">
<head>
<meta charset="utf-8">
<title>Cordova Peak Realty Group Inc. — Stationery</title>
<link rel="stylesheet" href="https://fonts.googleapis.com/css2?family=Cinzel:wght@400;700&family=Lato:wght@400;700&display=swap">
<style>
  :root {
    --bg: #3a3a3c;
    --paper: #ffffff;
    --orange: #f05a22;
    --ink: #3c3c3c;
    --muted: #8a8a8a;
  }
  * { box-sizing: border-box; margin: 0; padding: 0; }
  html, body { width: 1200px; height: 818px; overflow: hidden; }
  body {
    background: var(--bg);
    position: relative;
    font-family: "Lato", Arial, sans-serif;
    color: var(--ink);
  }
  .sheet { position: absolute; background: var(--paper); }

  .brand { display: flex; align-items: center; gap: 8px; }
  .brand-square { width: 14px; height: 14px; background: var(--orange); flex: none; }
  .brand-name {
    font-family: "Cinzel", Georgia, serif;
    font-weight: 700;
    color: var(--ink);
    line-height: 1.05;
    white-space: nowrap;
  }
  .brand-name .line2 { display: block; font-size: 0.42em; letter-spacing: 0.04em; }

  .divider { position: absolute; width: 2px; background: var(--orange); }
  .contact { position: absolute; font-style: normal; font-size: 7.5px; line-height: 1.55; color: var(--muted); white-space: nowrap; }
  .contact .lic { color: var(--orange); }

  /* Letterhead */
  .letterhead { left: 45px; top: 95px; width: 487px; height: 688px; }
  .letterhead .brand { position: absolute; left: 25px; top: 26px; }
  .letterhead .brand-name { font-size: 26px; }
  .letterhead .divider { left: 210px; top: 28px; height: 62px; }
  .letterhead .contact { left: 222px; top: 28px; }
  .letterhead .footer-band { position: absolute; left: 0; bottom: 0; width: 100%; height: 32px; background: var(--orange); }

  /* Envelope back */
  .envelope-back { left: 555px; top: 125px; width: 595px; height: 250px; }
  .envelope-back svg { position: absolute; left: 0; top: 0; }
  .envelope-back .flap-square { position: absolute; left: 287px; top: 50px; width: 20px; height: 20px; background: var(--paper); }

  /* Envelope front */
  .envelope-front { left: 475px; top: 250px; width: 663px; height: 250px; box-shadow: 0 2px 6px rgba(0,0,0,.25); }
  .envelope-front .brand { position: absolute; left: 22px; top: 24px; }
  .envelope-front .brand-name { font-size: 22px; }
  .envelope-front .divider { left: 190px; top: 26px; height: 56px; }
  .envelope-front .contact { left: 202px; top: 26px; font-size: 7px; }
  .envelope-front .footer-band { position: absolute; left: 0; bottom: 0; width: 100%; height: 28px; background: var(--orange); }

  /* Business cards */
  .card { position: absolute; top: 583px; width: 212px; height: 117px; background: var(--orange); color: #fff; }
  .card-front { left: 588px; }
  .card-front .card-title { position: absolute; left: 12px; top: 12px; font-family: "Cinzel", Georgia, serif; font-size: 9px; white-space: nowrap; }
  .card-front .card-contact { position: absolute; left: 12px; top: 40px; font-style: normal; font-size: 6.5px; line-height: 1.6; white-space: nowrap; }
  .card-front .logo-panel { position: absolute; right: 10px; top: 38px; width: 96px; height: 56px; background: var(--paper); display: flex; align-items: center; justify-content: center; }
  .card-front .brand-name { font-size: 14px; }
  .card-front .brand-square { width: 9px; height: 9px; }
  .card-front .brand { gap: 5px; }

  .card-back { left: 818px; }
  .card-back .programs { position: absolute; left: 12px; top: 14px; list-style: none; font-size: 6.5px; line-height: 1.7; }
  .card-back .programs li::before { content: "\25B8 "; }
  .card-back .logo-panel { position: absolute; right: 50px; bottom: 14px; width: 40px; height: 22px; background: var(--paper); display: flex; align-items: center; justify-content: center; }
  .card-back .brand-square { width: 8px; height: 8px; }
</style>
</head>
<body>

  <section class="sheet letterhead" aria-label="Letterhead">
    <div class="brand">
      <span class="brand-square"></span>
      <span class="brand-name">CORDOVA<span class="line2">Peak Realty Group Inc.</span></span>
    </div>
    <span class="divider"></span>
    <address class="contact">
      4236 Fernway Crest Blvd.<br>
      Marlow Springs, CA 90417<br>
      T 555.201.0148 | F 555.201.0173<br>
      Morvani@cordovapeak.com<br>
      www.cordovapeak.com<br>
      <span class="lic">Lic. DRE#07246318</span>
    </address>
    <div class="footer-band"></div>
  </section>

  <section class="sheet envelope-back" aria-label="Envelope back">
    <svg width="595" height="250" viewBox="0 0 595 250">
      <path d="M0 0 H595 V10 L310 88 Q297 92 284 88 L0 10 Z" fill="#f05a22"/>
    </svg>
    <span class="flap-square"></span>
  </section>

  <section class="sheet envelope-front" aria-label="Envelope front">
    <div class="brand">
      <span class="brand-square"></span>
      <span class="brand-name">CORDOVA<span class="line2">Peak Realty Group Inc.</span></span>
    </div>
    <span class="divider"></span>
    <address class="contact">
      4236 Fernway Crest Blvd.<br>
      Marlow Springs, CA 90417<br>
      T 555.201.0148 | F 555.201.0173<br>
      Morvani@cordovapeak.com<br>
      <span class="lic">Lic. DRE#07246318</span>
    </address>
    <div class="footer-band"></div>
  </section>

  <section class="card card-front" aria-label="Business card front">
    <p class="card-title">Cordova Peak Realty Group Inc.</p>
    <address class="card-contact">
      4236 Fernway Crest Blvd.<br>
      Marlow Springs, CA 90417<br>
      T 555.201.0148<br>
      Morvani@cordovapeak.com<br>
      DRE#07246318
    </address>
    <div class="logo-panel">
      <div class="brand">
        <span class="brand-square"></span>
        <span class="brand-name">CORDOVA<span class="line2">Peak Realty Group Inc.</span></span>
      </div>
    </div>
  </section>

  <section class="card card-back" aria-label="Business card back">
    <ul class="programs">
      <li>First time buyer Programs</li>
      <li>Multi-Unit property Programs</li>
      <li>Low down payment Programs</li>
      <li>$ 0 Closing costs available</li>
    </ul>
    <div class="logo-panel"><span class="brand-square"></span></div>
  </section>

</body>
</html>
```